Lucky Ridge Game Evenings Business Card Design

I need a business card for a fun casino entertainment business. I would like one side of the business card to convey the feel of a playing card similar to the playing card uploaded but with one logo placed horizontally across the card and the web address below it.
the information side can be slightly more plain, maybe just a stack of chips along one side or something with a casino feel.

Industry/Entity Type

Casino

Contact Information for Business Card

Lucky Ridge Game Evenings
Dev Marrowby
Director
0452 618290
dev@luckyridgefun.com.au

```html
<!DOCTYPE html>
<html lang="en">
<head>
<meta charset="utf-8">
<title>Lucky Ridge Game Evenings – Business Card</title>
<link rel="stylesheet" href="https://fonts.googleapis.com/css2?family=Noto+Sans:wght@400&display=swap">
<style>
  :root {
    --chip-lavender: #8f8fe6;
    --chip-pale: #c9c9f2;
    --card-white: #ffffff;
    --text-orange: #e2600f;
    --text-outline: #4a1c06;
  }
  html, body {
    margin: 0;
    padding: 0;
    width: 1200px;
    height: 741px;
    overflow: hidden;
    background: var(--card-white);
  }
  .card {
    position: relative;
    width: 1200px;
    height: 741px;
    overflow: hidden;
    background: var(--card-white);
  }
  .chip-stacks {
    position: absolute;
    inset: 0;
    background:
      radial-gradient(ellipse 300px 260px at 600px 760px, var(--chip-lavender) 0%, var(--chip-pale) 55%, rgba(255,255,255,0) 100%),
      linear-gradient(to right,
        var(--chip-lavender) 0%,
        var(--chip-pale) 18%,
        rgba(255,255,255,0.9) 30%,
        var(--card-white) 40%,
        var(--card-white) 60%,
        rgba(255,255,255,0.9) 70%,
        var(--chip-pale) 82%,
        var(--chip-lavender) 100%);
  }
  .details {
    position: absolute;
    inset: 0;
  }
  .details text {
    font-family: "Noto Sans", "Tahoma", sans-serif;
    fill: var(--text-orange);
    stroke: var(--text-outline);
    stroke-width: 2.4px;
    paint-order: stroke fill;
    text-anchor: middle;
  }
  .business-name, .person-line { font-size: 78px; }
  .phone { font-size: 88px; }
  .email { font-size: 58px; }
</style>
</head>
<body>
  <div class="card">
    <div class="chip-stacks" role="img" aria-label="Soft blurred stacks of lavender poker chips on both sides and at the bottom"></div>
    <svg class="details" width="1200" height="741" viewBox="0 0 1200 741">
      <text class="business-name" x="600" y="195">Lucky Ridge Game Evenings</text>
      <text class="person-line" x="600" y="297">Dev Marrowby Director</text>
      <text class="phone" x="600" y="449">0452 618290</text>
      <text class="email" x="600" y="589">dev@luckyridgefun.com.au</text>
    </svg>
  </div>
</body>
</html>
```